eBook Cover_H. Brückner-Lohm
Schnell und zuverlässoig,Änderungswünsche wurden umgehend ausgeführt. Vielen Dank für das tolle Cover zu meinem ersten Buch!
Zielgruppe
freie Roman-Autorin (Erstlingswerk)
Zielgruppe: Lesende (Erwachsene), Frauen
Charakterisierung: magisch-realistischer Familienroman, spielt im Europa der Jetzt-Zeit
Aufgabenstellung
Im ersten Schritt geht es um ein Cover für ein eBook, das aber bei Bedarf als Book on Demand gedruckt werden soll. Es wird daher später Anforderung bzgl. Dicke / Umfang des gedruckten Buches und einer Rückseite geben. Das gewählte Design soll dann dahingehend überarbeitet und finale Druckdaten zur Verfügung gestellt werden. Dies soll von vornherein berücksichtigt werden und im Preis enthalten sein.
Titel: Moos auf Moos, Wellen aus Glas
Autorinnenname: Hanna Brückner-Lohm
des weiteren auf dem Cover: Roman

```html
<!DOCTYPE html>
<html lang="de">
<head>
<meta charset="utf-8">
<title>Moos auf Moos, Wellen aus Glas – Hanna Brückner-Lohm</title>
<link href="https://fonts.googleapis.com/css2?family=Rubik+Dirt&family=Source+Sans+3:wght@400&family=Tinos&display=swap" rel="stylesheet">
<style>
  :root {
    --cover-bg: #231f20;
    --author-white: #f2f2f2;
    --title-yellow: #f4e52a;
    --ash-dark: #4a4a4a;
    --ash-light: #7a7a7a;
    --genre-white: #e8e8e8;
  }
  html, body {
    margin: 0;
    padding: 0;
    width: 800px;
    height: 1200px;
    overflow: hidden;
    background: var(--cover-bg);
  }
  .cover {
    position: relative;
    width: 800px;
    height: 1200px;
    background: var(--cover-bg);
    overflow: hidden;
  }
  .author {
    position: absolute;
    top: 124px;
    left: 0;
    width: 100%;
    text-align: center;
    margin: 0;
    font-family: "Source Sans 3", "Myriad Pro", sans-serif;
    font-weight: 400;
    font-size: 34px;
    letter-spacing: 0.5px;
    color: var(--author-white);
  }
  .title {
    position: absolute;
    top: 318px;
    left: 0;
    width: 100%;
    margin: 0;
    text-align: center;
    font-family: "Rubik Dirt", "Impact", sans-serif;
    font-weight: 400;
    font-size: 68px;
    line-height: 110px;
    color: var(--title-yellow);
    text-transform: uppercase;
  }
  .title-line {
    display: block;
    transform: scaleX(0.78);
    white-space: nowrap;
  }
  .ash-field {
    position: absolute;
    left: 196px;
    top: 690px;
    width: 492px;
    height: 280px;
  }
  .genre {
    position: absolute;
    top: 1112px;
    left: 0;
    width: 100%;
    margin: 0;
    text-align: center;
    font-family: "Tinos", "Times New Roman", serif;
    font-size: 27px;
    color: var(--genre-white);
  }
</style>
</head>
<body>
  <main class="cover">
    <p class="author">Hanna Brückner-Lohm</p>
    <h1 class="title">
      <span class="title-line">Moos auf Moos,</span>
      <span class="title-line">Wellen aus Glas</span>
    </h1>
    <svg class="ash-field" viewBox="0 0 492 280" role="img" aria-label="Grau verstreute Ascheflocken und Staubspuren">
      <defs>
        <radialGradient id="ashGlow" cx="50%" cy="50%" r="55%">
          <stop offset="0%" stop-color="var(--ash-light)"/>
          <stop offset="100%" stop-color="var(--ash-dark)"/>
        </radialGradient>
      </defs>
      <path d="M40 40 C120 10 330 8 440 30 C480 60 470 120 488 170 C470 220 420 262 300 270 C200 276 90 268 20 240 C0 190 14 130 6 90 C10 60 22 48 40 40 Z" fill="url(#ashGlow)" opacity="0.85"/>
    </svg>
    <p class="genre">Roman</p>
  </main>
</body>
</html>
```